Billboard Design for Vantro Hub

Vantro Hub is a group buying site similar to plimzo.net. Everyday we offer consumers in Guatemala and El Salvador enormous discounts in salons, restaurants, hotels, and other fun activities. Our target market are middle-class consumers, especially women

```html
<!DOCTYPE html>
<html lang="es">
<head>
<meta charset="utf-8">
<title>Vantro Hub – Billboard</title>
<link rel="stylesheet" href="https://fonts.googleapis.com/css2?family=Cabin:wght@400;700&family=Yellowtail&display=swap">
<style>
  :root {
    --page-bg: #ffffff;
    --sky-top: #03aef0;
    --sky-bottom: #1b7fd8;
    --bar-bg: #115f90;
    --bar-text: #cdeaf8;
    --headline: #ffffff;
    --brand: #0d3c7e;
    --frame: #ffffff;
    --shadow: rgba(0, 0, 0, 0.55);
  }
  html, body {
    margin: 0;
    padding: 0;
    width: 1200px;
    height: 848px;
    overflow: hidden;
    background: var(--page-bg);
  }
  .canvas {
    position: relative;
    width: 1200px;
    height: 848px;
  }
  .billboard {
    position: absolute;
    left: 23px;
    top: 102px;
    width: 1131px;
    height: 472px;
    background: linear-gradient(180deg, var(--sky-top) 0%, var(--sky-bottom) 100%);
    box-shadow: 8px 10px 10px var(--shadow);
    overflow: hidden;
  }
  .headline {
    position: absolute;
    margin: 0;
    font-family: "Yellowtail", cursive;
    font-weight: 400;
    color: var(--headline);
    line-height: 1;
  }
  .headline-line1 { left: 80px; top: 34px; font-size: 72px; }
  .headline-line2 { left: 352px; top: 100px; font-size: 72px; }
  .photo {
    position: absolute;
    border: 4px solid var(--frame);
    box-shadow: 2px 3px 5px rgba(0,0,0,0.35);
    box-sizing: border-box;
  }
  .photo-dining {
    left: 170px; top: 165px; width: 150px; height: 115px;
    background: linear-gradient(135deg, #7a4a2a, #d9a86a 55%, #f3e6d0);
  }
  .photo-spa {
    left: 336px; top: 203px; width: 142px; height: 116px;
    background: linear-gradient(135deg, #f4e2d6, #e9c2a6 55%, #ffffff);
  }
  .photo-pool {
    left: 495px; top: 244px; width: 142px; height: 114px;
    background: linear-gradient(180deg, #8fc6ee 0%, #e8dcc6 40%, #2aa5e0 65%, #0b86c9 100%);
  }
  .brand {
    position: absolute;
    right: 121px;
    top: 98px;
    margin: 0;
    font-family: "Cabin", sans-serif;
    font-weight: 700;
    font-size: 86px;
    line-height: 1.38;
    color: var(--brand);
    text-align: right;
  }
  .brand span { display: block; }
  .offer-bar {
    position: absolute;
    left: 0;
    bottom: 0;
    width: 100%;
    height: 74px;
    background: var(--bar-bg);
  }
  .offer-text {
    position: absolute;
    left: 51px;
    top: 12px;
    margin: 0;
    font-family: "Cabin", sans-serif;
    font-weight: 400;
    font-size: 39px;
    line-height: 1.2;
    color: var(--bar-text);
    white-space: nowrap;
  }
</style>
</head>
<body>
<div class="canvas">
  <section class="billboard">
    <h1 class="headline headline-line1">Disfrutaa tu ciudad</h1>
    <p class="headline headline-line2">por menos</p>

    <div class="photo photo-dining" role="img" aria-label="Foto de un restaurante con mesa servida"></div>
    <div class="photo photo-spa" role="img" aria-label="Foto de un masaje facial en un spa"></div>
    <div class="photo photo-pool" role="img" aria-label="Foto de un hotel con piscina"></div>

    <h2 class="brand"><span>Vantro</span><span>Hub</span></h2>

    <div class="offer-bar">
      <p class="offer-text">No tipierdas la oferta de hoy en - www.vantrohub.net</p>
    </div>
  </section>
</div>
</body>
</html>
```